VocaTerrania Community/ Talent Gallery

VocaTerrania is developing a collaborative career course, with coaching and community exchange. Goal is to offer a platform where talented candidates can show their expertise and find projects, partners, and develop their online portfolios!

Here is a good example of the type of thing we hope to create with focus on sustainability focused talent to task matching
http://www.harrowbyquill.example/global-themes/employment-and-growth/connecting-talent-with-opportunity-in-the-digital-age

We hope to have a "grid style" gallery where it is easy to search by talent types and focus areas within the scope of "Sustainability" issues...Food/Water/Energy, Public Health, Technology, Sustainable Cities, Infrastructure, Education, Policy, Emerging Economies, Ecosystems, Social Innovation, inclusive Security, Equity Issues. For each topic/ header we hope to have candidates post their completed portfolios to exhibit resumes, biography, a case study... they may actually prepare these on other sites, but can link in OR alternately that they can easily create here, similar to "posy.lan" ....

Hope to include a blog space titled "Walking the Ridge", where people can mix it up across these topic issues as they are interdependent and often require partners across discipline areas! If possible another area where jobs related to these issues may be posted as project or job opportunities by potential employers.

If there is a way to create a feed from various job sites that already exist...like Nuvol...or http://www.verdantledgerhub.example/ that would be super great. Again...sort of a portal connection to bridge the gap ....instead of candidates having to search all the time, we are hoping they can advertise their talent and employers may search here for these well presented portfolios!

Target Market(s)

Educators, Students, Career Transitioners, Employers, Professional Associations, Talent Recruiters with focus on Sustainability related Talent to Task matching!

Industry/Entity Type

Sustainability

Number of Pages Required

4 page

Font styles to use
Sans Serif

Colors
3176b5
32b8a4
add136

Requirements
Must have
• Not sure about the coded/ uncoded option here....
• Must have - grid style area where Sustainability Professionals with varied focus areas can exhibit their talent portfolios
• appear as a Talent Gallery that starts with photos & obvious organization...other tabs to be in a menu.
• ability to search both talent and task opportunity areas to help coaches or community members make matches....some topic focused category or tag words to help make them searchable...???
• consistent professional styling to existing website and new pixelmarket postcard shared in brief/ images area
• Interactive blog space where articles, issues may be posted, discussed
• Bulletin board or feed for project opportunities to be posted where candidates may locate them and/or employers may express specific "call" for talent..These may be Short term Internships, Projects, Consulting Team Opportunity, or Jobs/ part time to full time....
Nice to have
• A calendar area where we can post networking opportunities, issues presentations where potential partners can meet the next generation leaders, attend a forum or webinar presentation.
Should not have
• Too much text on front page...Should be clean design,

```html
<!DOCTYPE html>
<html lang="en">
<head>
<meta charset="utf-8">
<title>VocaTerrania – Collaborative Career Course</title>
<link rel="stylesheet" href="https://fonts.googleapis.com/css2?family=Open+Sans:wght@400;600;700&display=swap">
<style>
:root{
  --teal:#1b8f8c;
  --teal-dark:#14706e;
  --aqua:#32b8a4;
  --blue:#3176b5;
  --green:#8dc63f;
  --lime:#add136;
  --ink:#222b33;
  --muted:#5d666e;
  --navy:#18283a;
  --navy-deep:#101c29;
  --paper:#ffffff;
  --mist:#f2f4f5;
}
*{box-sizing:border-box;margin:0;padding:0}
html,body{width:1200px;height:3928px;overflow:hidden}
body{font-family:"Open Sans",Arial,sans-serif;color:var(--ink);background:var(--paper);position:relative}
a{color:inherit;text-decoration:none}
.btn{display:inline-block;background:var(--green);color:#fff;font-weight:600;font-size:16px;padding:8px 22px 8px 40px;border-radius:18px;position:relative}
.btn::before{content:"";position:absolute;left:10px;top:50%;width:20px;height:20px;margin-top:-10px;border-radius:50%;background:rgba(255,255,255,.35)}
.section-title{text-align:center;font-size:42px;font-weight:600;color:var(--ink)}
.section-title span{color:var(--teal)}
.title-rule{display:block;margin:12px auto 0;width:140px;height:16px}

/* header */
.site-header{position:absolute;top:0;left:0;width:1200px;height:72px;background:#fff;box-shadow:0 2px 4px rgba(0,0,0,.06);z-index:2}
.brand{position:absolute;left:108px;top:10px;display:flex;align-items:center;gap:12px}
.brand-mark{width:52px;height:52px;border-radius:50%;background:var(--teal)}
.brand-name{font-size:28px;font-weight:700;color:var(--blue)}
.topbar{position:absolute;right:96px;top:4px;display:flex;align-items:center;gap:22px;font-size:13px;color:var(--muted)}
.topbar .item{display:flex;align-items:center;gap:6px}
.login{background:var(--green);color:#fff;font-weight:600;padding:4px 18px;border-radius:3px}
.main-nav{position:absolute;right:96px;top:44px;display:flex;gap:34px;font-size:16px;font-weight:600}
.main-nav a.current{color:var(--teal);border-bottom:2px solid var(--teal)}

/* hero */
.hero{position:absolute;top:72px;left:0;width:1200px;height:528px;background:radial-gradient(ellipse at 50% 55%,#cfd6cf 0%,#9aa39c 45%,#5e6862 100%)}
.hero-text{position:absolute;left:0;right:0;top:340px;text-align:center;color:#fff}
.hero-text h1{font-size:36px;font-weight:600;line-height:1.3;text-shadow:0 2px 6px rgba(0,0,0,.45)}
.hero-text .btn{margin-top:22px}

/* mission */
.mission{position:absolute;top:600px;left:0;width:1200px;height:480px}
.mission-copy{position:absolute;left:100px;top:136px;width:640px}
.mission-copy h2{font-size:40px;font-weight:600}
.mission-copy h2 span{color:var(--teal)}
.mission-copy .rule{width:90px;height:4px;background:var(--teal);margin:12px 0 26px}
.mission-copy p{font-size:15px;line-height:1.7;color:var(--muted)}
.mission-copy .btn{margin-top:26px}
.offer-panel{position:absolute;left:800px;top:88px;width:400px;height:392px;background:var(--teal);padding:36px 0 0 40px}
.offer-panel li{list-style:none;display:flex;align-items:center;gap:20px;color:#fff;font-size:18px;font-weight:600;height:82px}
.offer-panel svg{width:40px;height:40px}

/* course */
.course{position:absolute;top:1080px;left:0;width:1200px;height:680px;background:var(--mist)}
.course .section-title{margin-top:66px}
.course-intro{width:800px;margin:40px auto 0;text-align:center;font-size:15px;line-height:1.65;color:var(--muted)}
.course .btn-row{text-align:center;margin-top:22px}
.phases{position:absolute;left:100px;top:328px;width:1000px;display:flex;gap:16px}
.phase{flex:1;background:#fff;text-align:center;padding-bottom:12px}
.phase .photo{height:196px}
.phase .dot{width:36px;height:36px;border-radius:50%;background:var(--teal);margin:-18px auto 0;position:relative;border:4px solid #fff}
.phase h3{font-size:20px;font-weight:700;margin-top:6px;letter-spacing:.5px}
.phase p{font-size:12px;color:var(--muted);margin-top:4px}

/* gallery */
.gallery{position:absolute;top:1760px;left:0;width:1200px;height:640px;background:var(--teal)}
.gallery .section-title{color:#fff;margin-top:80px}
.gallery .section-title span{color:#fff}
.tile-grid{position:absolute;left:100px;top:208px;width:1000px;height:400px;display:grid;gap:8px;
  grid-template-columns:220px 352px 224px 1fr;grid-template-rows:1fr 1fr}
.tile{position:relative;overflow:hidden}
.tile .label{position:absolute;left:0;right:0;bottom:0;background:rgba(0,0,0,.55);color:#fff;font-size:13px;font-weight:600;text-align:center;padding:5px}
.tile.tall{grid-row:1/3}
.tile-split{display:grid;grid-template-columns:1fr 1fr;gap:8px}
.view-more{background:var(--navy-deep);color:#fff;font-weight:700;font-size:17px;display:flex;align-items:center;justify-content:center;text-align:center;line-height:1.3}

/* coaches */
.coaches{position:absolute;top:2400px;left:0;width:1200px;height:500px}
.coaches .section-title{margin-top:90px}
.coach{position:absolute;top:220px;display:flex;gap:24px}
.coach .portrait{width:248px;height:228px}
.coach .bio{width:220px}
.coach h3{font-size:18px;font-weight:700}
.coach p{font-size:13px;line-height:1.6;color:var(--muted);margin-top:8px}
.coach .more{font-size:13px;font-weight:600;margin-top:8px;display:block}

/* blog */
.ridge{position:absolute;top:2900px;left:0;width:1200px;height:540px;background:var(--teal)}
.ridge .section-title{color:#fff;margin-top:72px}
.posts{position:absolute;left:100px;top:188px;width:1000px;display:flex;gap:48px}
.post{flex:1;color:#fff}
.post .photo{height:176px;position:relative}
.post .date{position:absolute;left:10px;top:0;width:52px;background:var(--teal-dark);text-align:center;font-weight:700;line-height:1.1;padding:6px 0}
.post .date b{display:block;font-size:22px}
.post .date small{font-size:11px}
.post h3{font-size:16px;font-weight:700;margin-top:14px}
.post p{font-size:12px;line-height:1.55;margin-top:8px;opacity:.9}
.post .more{display:inline-block;margin-top:12px;background:var(--navy-deep);font-size:12px;padding:4px 14px}

/* footer */
.footer-nav{position:absolute;top:3440px;left:0;width:1200px;height:80px;display:flex;justify-content:center;align-items:center;gap:80px;font-size:17px;font-weight:600}
.footer-nav a.current{color:var(--teal);border-bottom:2px solid var(--teal)}
.site-footer{position:absolute;top:3520px;left:0;width:1200px;height:380px;background:var(--navy)}
.foot-col{position:absolute;top:42px;color:#c9d3dc;font-size:13px}
.foot-col h4{font-size:20px;font-weight:600;color:var(--aqua);margin-bottom:10px}
.foot-col .rule{height:1px;background:rgba(255,255,255,.25);margin-bottom:22px}
.contact-row{display:flex;gap:10px;align-items:flex-start;margin-bottom:22px;line-height:1.5}
.contact-row svg{flex:none;width:16px;height:16px;margin-top:2px}
.field{width:260px;height:28px;background:#fff;color:#8a929a;font-size:12px;padding:6px 10px;margin-bottom:8px}
.field.area{height:40px}
.submit{display:inline-block;background:var(--teal);color:#fff;font-weight:600;padding:5px 22px}
.feed h5{color:#fff;font-size:12px;font-weight:700;margin-bottom:12px}
.feed li{list-style:none;margin-bottom:14px;line-height:1.45;padding-left:12px;position:relative}
.feed li::before{content:"";position:absolute;left:0;top:7px;width:5px;height:5px;background:var(--aqua)}
.socials{position:absolute;right:100px;top:318px;display:flex;gap:10px}
.socials span{width:26px;height:26px;border-radius:50%;background:var(--blue)}
.copyright{position:absolute;top:3900px;left:0;width:1200px;height:28px;background:var(--navy-deep);color:#c9d3dc;font-size:12px;padding:6px 100px}
</style>
</head>
<body>

<header class="site-header">
  <a class="brand" href="#"><span class="brand-mark"></span><span class="brand-name">VocaTerrania</span></a>
  <div class="topbar">
    <span class="item"><svg width="12" height="12" viewBox="0 0 24 24"><path fill="#1b8f8c" d="M6.6 10.8a15 15 0 006.6 6.6l2.2-2.2a1 1 0 011-.3 11 11 0 003.6.6 1 1 0 011 1V20a1 1 0 01-1 1A17 17 0 013 4a1 1 0 011-1h3.5a1 1 0 011 1 11 11 0 00.6 3.6 1 1 0 01-.3 1z"/></svg>202-555-0148</span>
    <span class="item"><svg width="12" height="12" viewBox="0 0 24 24"><path fill="#1b8f8c" d="M2 5h20v14H2zm2 2v.5l8 5 8-5V7z"/></svg>info@vocaterrania.example</span>
    <a class="login" href="#">Log In</a>
  </div>
  <nav class="main-nav">
    <a class="current" href="#">Home</a><a href="#">About Us</a><a href="#">Services</a><a href="#">Blog</a><a href="#">Contact Us</a>
  </nav>
</header>

<section class="hero" role="img" aria-label="Black and white photo of cupped hands holding a young green seedling">
  <div class="hero-text">
    <h1>We Are Developing A Collaborative Career Course<br>With Coaching And Community Exchange</h1>
    <a class="btn" href="#">Get Start Now</a>
  </div>
</section>

<section class="mission">
  <div class="mission-copy">
    <h2>Our <span>Mission &amp; Philosophy</span></h2>
    <div class="rule"></div>
    <p>Our mission is to cultivate a community of learning and professional practice that supports career transitions and next-generation leadership for sustainable solutions. We balance economic, environmental and equity goals through global exchange, individual inquiry and creative talent development, guided by professional coaches and a wide network of practitioners from sustainability-focused organizations.</p>
    <a class="btn" href="#">Read More</a>
  </div>
  <ul class="offer-panel">
    <li><svg viewBox="0 0 40 40"><circle cx="14" cy="12" r="6" fill="#fff"/><circle cx="28" cy="14" r="5" fill="#fff"/><path d="M3 34c0-8 5-13 11-13s11 5 11 13zM23 34c0-5 2-9 5-11 5 0 9 4 9 11z" fill="#fff"/></svg>Next Generation Talent</li>
    <li><svg viewBox="0 0 40 40"><path d="M4 8h14a4 4 0 014 4v22a3 3 0 00-3-3H4zM36 8H24a2 2 0 00-2 2v24a3 3 0 013-3h11z" fill="#fff"/></svg>Courses</li>
    <li><svg viewBox="0 0 40 40"><rect x="5" y="7" width="30" height="20" rx="2" fill="#fff"/><rect x="13" y="30" width="14" height="3" fill="#fff"/></svg>Online Coaching</li>
    <li><svg viewBox="0 0 40 40"><circle cx="12" cy="11" r="5" fill="#fff"/><circle cx="28" cy="11" r="5" fill="#fff"/><path d="M3 33c0-7 4-12 9-12s9 5 9 12zM19 33c0-7 4-12 9-12s9 5 9 12z" fill="#fff"/></svg>In-Person Coaching</li>
  </ul>
</section>

<section class="course">
  <h2 class="section-title">Four Phase <span>Career Course</span></h2>
  <svg class="title-rule" viewBox="0 0 140 16"><line x1="0" y1="8" x2="58" y2="8" stroke="#1b8f8c" stroke-width="2"/><line x1="82" y1="8" x2="140" y2="8" stroke="#1b8f8c" stroke-width="2"/><circle cx="70" cy="8" r="6" fill="#1b8f8c"/></svg>
  <p class="course-intro">Through a proven four-phase process integrating principles of lifelong learning, career transitions, entrepreneurship, change management and innovation, our interdisciplinary collaborative course is designed to guide you through creative change for career, lifestyle and next-generation leadership.</p>
  <div class="btn-row"><a class="btn" href="#">Read More</a></div>
  <div class="phases">
    <article class="phase"><div class="photo" role="img" aria-label="Team hands joining colourful puzzle pieces" style="background:linear-gradient(135deg,#c6d0d8,#8c9cab)"></div><div class="dot"></div><h3>CLARIFY</h3><p>Personal Profile, Vision &amp; Mission</p></article>
    <article class="phase"><div class="photo" role="img" aria-label="Professionals in conversation around a table" style="background:linear-gradient(135deg,#b9c6d4,#6e879c)"></div><div class="dot"></div><h3>COMMUNICATE</h3><p>Personal Profile, Vision &amp; Mission</p></article>
    <article class="phase"><div class="photo" role="img" aria-label="Group of colleagues stacking hands together" style="background:linear-gradient(135deg,#d6d9de,#99a3ad)"></div><div class="dot"></div><h3>COLLABORATE</h3><p>Personal Profile, Vision &amp; Mission</p></article>
    <article class="phase"><div class="photo" role="img" aria-label="Hand sketching a design on a glass board" style="background:linear-gradient(135deg,#dfe8ef,#9fb4c6)"></div><div class="dot"></div><h3>CREATE</h3><p>Personal Profile, Vision &amp; Mission</p></article>
  </div>
</section>

<section class="gallery">
  <h2 class="section-title">Our <span>Gallery</span></h2>
  <svg class="title-rule" viewBox="0 0 140 16"><line x1="0" y1="8" x2="58" y2="8" stroke="#fff" stroke-width="2"/><line x1="82" y1="8" x2="140" y2="8" stroke="#fff" stroke-width="2"/><circle cx="70" cy="8" r="6" fill="#fff"/></svg>
  <div class="tile-grid">
    <div class="tile tall" role="img" aria-label="Construction crane silhouetted at sunset" style="background:linear-gradient(180deg,#e3a24a,#7a3f18)"><span class="label">Infrastructure</span></div>
    <div class="tile" role="img" aria-label="Wind turbines and produce representing food, water and energy" style="background:linear-gradient(135deg,#dfe6ea,#9aa8b2)"><span class="label">Food/ Water/ Energy</span></div>
    <div class="tile" role="img" aria-label="Medical staff and health equipment" style="grid-column:3;background:linear-gradient(135deg,#7fa86a,#3d6d57)"><span class="label">Sustainable Cities</span></div>
    <div class="tile" role="img" aria-label="Students learning together" style="background:linear-gradient(135deg,#d8c7b0,#9b8468)"><span class="label">Education</span></div>
    <div class="tile" role="img" aria-label="Health care workers" style="grid-column:2;grid-row:2;background:linear-gradient(135deg,#9ec4df,#4d7fa6)"><span class="label">Public Health</span></div>
    <div class="tile" role="img" aria-label="Glowing digital network over a city" style="grid-column:3;grid-row:2;background:linear-gradient(135deg,#2b4f8a,#122544)"><span class="label">Technology</span></div>
    <div class="tile-split" style="grid-column:4;grid-row:2">
      <div class="tile" role="img" aria-label="Policy meeting" style="background:linear-gradient(135deg,#c9ccd2,#7d8591)"></div>
      <a class="view-more" href="#">View<br>More</a>
    </div>
  </div>
</section>

<section class="coaches">
  <h2 class="section-title">Our <span>Coaches</span></h2>
  <svg class="title-rule" viewBox="0 0 140 16"><line x1="0" y1="8" x2="58" y2="8" stroke="#1b8f8c" stroke-width="2"/><line x1="82" y1="8" x2="140" y2="8" stroke="#1b8f8c" stroke-width="2"/><circle cx="70" cy="8" r="6" fill="#1b8f8c"/></svg>
  <article class="coach" style="left:100px">
    <div class="portrait" role="img" aria-label="Portrait of coach Marguerite Ollander Vaske" style="background:linear-gradient(135deg,#8a7a66,#3e342a)"></div>
    <div class="bio">
      <h3>Marguerite Ollander Vaske</h3>
      <p>Certified Educator, Career Leadership Development Consultant with over 30 years of experience in non-profit, higher education and NGO organizations, collaborating across disciplines and sectors.</p>
      <a class="more" href="#">Read More &rsaquo;</a>
    </div>
  </article>
  <article class="coach" style="left:628px">
    <div class="bio">
      <h3>Delia Strathmore</h3>
      <p>Delia Strathmore is a seasoned communicator and coach. She is the president and principal of a strategic search firm and Career Advancement Services, and a Certified Master Coach.</p>
      <a class="more" href="#">Read More &rsaquo;</a>
    </div>
    <div class="portrait" role="img" aria-label="Portrait of coach Delia Strathmore" style="background:linear-gradient(135deg,#9aa2aa,#4a525a)"></div>
  </article>
</section>

<section class="ridge">
  <h2 class="section-title">Walking The Ridge</h2>
  <svg class="title-rule" viewBox="0 0 140 16"><line x1="0" y1="8" x2="58" y2="8" stroke="#fff" stroke-width="2"/><line x1="82" y1="8" x2="140" y2="8" stroke="#fff" stroke-width="2"/><circle cx="70" cy="8" r="6" fill="#fff"/></svg>
  <div class="posts">
    <article class="post">
      <div class="photo" role="img" aria-label="Stacked stones balanced on a beach" style="background:linear-gradient(135deg,#c9c3b8,#6f685e)"><span class="date"><b>23</b><small>JUN</small></span></div>
      <h3>Ecosystem Insights for Leaders</h3>
      <p>As we all bring our talents to complex systems, leaders need fresh frameworks to see how people, places and resources connect.</p>
      <a class="more" href="#">Read More</a>
    </article>
    <article class="post">
      <div class="photo" role="img" aria-label="Book cover on the age of sustainable development" style="background:linear-gradient(135deg,#b3543a,#4a1f14)"><span class="date"><b>23</b><small>JUN</small></span></div>
      <h3>Sustainable Development ?</h3>
      <p>A recently published book explores the age of sustainable development and offers a critical synthesis of ideas.</p>
      <a class="more" href="#">Read More</a>
    </article>
    <article class="post">
      <div class="photo" role="img" aria-label="Platter of colourful grilled food" style="background:linear-gradient(135deg,#e0a04a,#8c3a1e)"><span class="date"><b>23</b><small>JUN</small></span></div>
      <h3>Food Security</h3>
      <p>People can do just one of the small things to help, and together those choices can create lasting change everywhere.</p>
      <a class="more" href="#">Read More</a>
    </article>
  </div>
</section>

<nav class="footer-nav">
  <a class="current" href="#">Home</a><a href="#">About Us</a><a href="#">Services</a><a href="#">Blog</a><a href="#">Contact Us</a>
</nav>

<footer class="site-footer">
  <div class="foot-col" style="left:100px;width:280px">
    <h4>Contact Details</h4><div class="rule"></div>
    <div class="contact-row"><svg viewBox="0 0 24 24"><path fill="#32b8a4" d="M12 2a7 7 0 00-7 7c0 5 7 13 7 13s7-8 7-13a7 7 0 00-7-7zm0 9.5A2.5 2.5 0 1112 6a2.5 2.5 0 010 5.5z"/></svg><span>4812 Larkspur Glen Lane,<br>Brookhaven, MD 20807</span></div>
    <div class="contact-row"><svg viewBox="0 0 24 24"><path fill="#32b8a4" d="M6.6 10.8a15 15 0 006.6 6.6l2.2-2.2a1 1 0 011-.3 11 11 0 003.6.6 1 1 0 011 1V20a1 1 0 01-1 1A17 17 0 013 4a1 1 0 011-1h3.5a1 1 0 011 1 11 11 0 00.6 3.6 1 1 0 01-.3 1z"/></svg><span>202-555-0148</span></div>
    <div class="contact-row"><svg viewBox="0 0 24 24"><rect x="3" y="5" width="18" height="14" fill="#32b8a4"/></svg><span>202-555-0149</span></div>
    <div class="contact-row"><svg viewBox="0 0 24 24"><path fill="#32b8a4" d="M2 5h20v14H2zm2 2v.5l8 5 8-5V7z"/></svg><span>info@vocaterrania.example</span></div>
  </div>
  <div class="foot-col" style="left:460px;width:280px">
    <h4>Quick Inquiry</h4><div class="rule"></div>
    <div class="field">Name</div>
    <div class="field">Email</div>
    <div class="field area">Message</div>
    <a class="submit" href="#">Submit</a>
  </div>
  <div class="foot-col feed" style="left:820px;width:280px">
    <h4>View Feeds</h4><div class="rule"></div>
    <h5>CANOPY CAREERS BOARD</h5>
    <ul>
      <li>Education Development Coordinator<br>Urban Forest Council</li>
      <li>Environmental Communications Specialist<br>Riverbend Climate Group, Inc.</li>
      <li>Solar Grant Analyst<br>Fieldstone, Inc.</li>
    </ul>
  </div>
  <div class="socials"><span></span><span></span><span></span><span></span></div>
</footer>

<div class="copyright">Copyright © 2016 VocaTerrania. All Rights Reserved.</div>

</body>
</html>
```